Accounting business needs business card

I have a business card but need something better. I want the colour changed and the design to be better. I have uploaded a picture of my new sign that is grey in colour, i would like to incorporate these colours.

```html
<!DOCTYPE html>
<html lang="en">
<head>
<meta charset="utf-8">
<title>Alto Tax – Business Card</title>
<link href="https://fonts.googleapis.com/css2?family=Montserrat:wght@500;600;700&family=Quicksand:wght@500;600&display=swap" rel="stylesheet">
<style>
  :root {
    --backdrop: #14233a;
    --ink: #2b2c2e;
    --ink-soft: #3a3b3d;
    --metal-light: #d3d6db;
    --metal-mid: #bfc3c9;
    --metal-dark: #aeb2b9;
    --band-grey: #e1e1e1;
    --card-white: #ffffff;
    --divider: #c9c9c9;
    --badge-fill: #c4c6ca;
    --badge-fill-dark: #a9acb1;
    --icon-bg: #d9dadc;
  }
  * { box-sizing: border-box; margin: 0; padding: 0; }
  html, body {
    width: 1200px; height: 825px; overflow: hidden;
    background: var(--backdrop);
  }
  .canvas { position: relative; width: 1200px; height: 825px; }

  .card {
    position: absolute; left: 290px; width: 620px; height: 369px;
    overflow: hidden;
    box-shadow: 0 12px 30px rgba(0,0,0,.35);
  }

  /* Front */
  .card--front {
    top: 30px;
    background:
      repeating-linear-gradient(180deg, rgba(255,255,255,.08) 0 1px, rgba(0,0,0,0) 1px 3px),
      linear-gradient(100deg, var(--metal-mid) 0%, var(--metal-light) 35%, var(--metal-mid) 60%, var(--metal-dark) 100%);
  }
  .front-mark {
    position: absolute; left: 252px; top: 101px;
    width: 115px; height: 115px;
    border: 3px solid var(--ink); border-radius: 50%;
  }
  .front-name {
    position: absolute; left: 0; right: 0; top: 231px;
    text-align: center;
    font-family: "Montserrat", sans-serif; font-weight: 600;
    font-size: 38px; letter-spacing: .42em; text-indent: .42em;
    color: var(--ink);
  }

  /* Back */
  .card--back { top: 426px; background: var(--card-white); }
  .back-band {
    position: absolute; left: 0; top: 0; width: 100%; height: 184px;
    background: var(--band-grey);
  }
  .back-mark {
    position: absolute; left: 107px; top: 46px;
    width: 68px; height: 68px;
    border: 2px solid var(--ink); border-radius: 50%;
  }
  .back-name {
    position: absolute; left: 54px; top: 122px;
    font-family: "Montserrat", sans-serif; font-weight: 600;
    font-size: 20px; letter-spacing: .42em;
    color: var(--ink);
  }
  .band-divider {
    position: absolute; left: 311px; top: 48px;
    width: 2px; height: 97px; background: var(--divider);
  }

  /* Partner badges: plain neutral placeholders */
  .badge {
    position: absolute;
    background: var(--badge-fill);
  }
  .badge--registry {
    left: 347px; top: 67px; width: 55px; height: 55px; border-radius: 50%;
  }
  .badge--association {
    left: 421px; top: 73px; width: 94px; height: 42px;
    background: var(--badge-fill-dark);
  }
  .badge--software {
    left: 532px; top: 74px; width: 41px; height: 41px; border-radius: 50%;
  }
  .badge-caption {
    position: absolute; left: 340px; top: 129px; width: 70px;
    text-align: center;
    font-family: "Quicksand", sans-serif; font-weight: 600;
    font-size: 6.5px; line-height: 8px; color: var(--ink);
  }

  .person {
    position: absolute; left: 54px; top: 234px;
    font-family: "Montserrat", sans-serif; font-weight: 700;
    font-size: 20px; letter-spacing: .2em; color: var(--ink);
  }
  .credentials {
    position: absolute; left: 54px; top: 271px;
    font-family: "Quicksand", sans-serif; font-weight: 500;
    font-size: 14px; line-height: 17px; letter-spacing: .02em;
    color: var(--ink-soft);
  }

  .contact-list {
    position: absolute; left: 397px; top: 236px; list-style: none;
    font-family: "Quicksand", sans-serif; font-weight: 500;
    font-size: 14px; color: var(--ink-soft);
  }
  .contact-item {
    display: flex; align-items: center; height: 20px; margin-bottom: 6px;
  }
  .contact-icon {
    width: 20px; height: 20px; margin-right: 9px; flex: none;
    border-radius: 50%; background: var(--icon-bg);
    display: flex; align-items: center; justify-content: center;
  }
  .contact-icon svg { width: 11px; height: 11px; }
</style>
</head>
<body>
<main class="canvas">

  <section class="card card--front" aria-label="Business card front">
    <div class="front-mark"></div>
    <p class="front-name">ALTO TAX</p>
  </section>

  <section class="card card--back" aria-label="Business card back">
    <div class="back-band"></div>
    <div class="back-mark"></div>
    <p class="back-name">ALTO TAX</p>
    <div class="band-divider"></div>

    <div class="badge badge--registry" role="img" aria-label="Registered tax agent badge"></div>
    <p class="badge-caption">Tax agent<br>10293847</p>
    <div class="badge badge--association" role="img" aria-label="Professional accounting body badge"></div>
    <div class="badge badge--software" role="img" aria-label="Accounting software partner badge"></div>

    <h1 class="person">LIAM HARTWELL</h1>
    <p class="credentials">CPA, MTAX, BCOM (Acc &amp; Fin)<br>Taxation &amp; Business Accountant</p>

    <ul class="contact-list">
      <li class="contact-item">
        <span class="contact-icon">
          <svg viewBox="0 0 24 24"><path fill="#2b2c2e" d="M6.6 10.8a15.1 15.1 0 0 0 6.6 6.6l2.2-2.2c.3-.3.7-.4 1-.2 1.1.4 2.3.6 3.6.6.6 0 1 .4 1 1V20c0 .6-.4 1-1 1A17 17 0 0 1 3 4c0-.6.4-1 1-1h3.5c.6 0 1 .4 1 1 0 1.3.2 2.5.6 3.6.1.3 0 .7-.2 1z"/></svg>
        </span>0400 555 018
      </li>
      <li class="contact-item">
        <span class="contact-icon">
          <svg viewBox="0 0 24 24"><path fill="#2b2c2e" d="M2 5h20v14H2z"/><path fill="none" stroke="#d9dadc" stroke-width="1.8" d="M2.5 5.5 12 13l9.5-7.5"/></svg>
        </span>liam@altotax.com.au
      </li>
      <li class="contact-item">
        <span class="contact-icon">
          <svg viewBox="0 0 24 24" fill="none" stroke="#2b2c2e" stroke-width="2"><circle cx="12" cy="12" r="9"/><path d="M3 12h18M12 3c3 3 3 15 0 18M12 3c-3 3-3 15 0 18"/></svg>
        </span>www.altotax.com.au
      </li>
    </ul>
  </section>

</main>
</body>
</html>
```